Continuation of "Why Choose Us" animated gif banners campaign

The original project would not allow me to select any more designs, so I started this new project so you can submit your designs and I will purchase them.

Thanks!

```html
<!DOCTYPE html>
<html lang="en">
<head>
<meta charset="utf-8">
<title>Why Choose Us – Banner Frames</title>
<link rel="stylesheet" href="https://fonts.googleapis.com/css2?family=Rubik:wght@700;800&display=swap">
<style>
  :root {
    --page-bg: #ececec;
    --banner-bg: #ffffff;
    --title-blue: #3d78b5;
    --label-blue: #3a5fd0;
    --icon-blue: #3d78b5;
    --pale-line: #b9dde6;
    --orbit-line: #dcebef;
    --ring-outer: #cfe0ee;
    --ring-inner: #8ccaf6;
    --shadow: rgba(0, 0, 0, 0.22);
  }
  * { box-sizing: border-box; margin: 0; padding: 0; }
  html, body {
    width: 1060px;
    height: 1200px;
    overflow: hidden;
    background: var(--page-bg);
    font-family: "Rubik", Arial, sans-serif;
  }
  .stage { position: relative; width: 1060px; height: 1200px; }

  .banner {
    position: absolute;
    left: 35px;
    width: 981px;
    height: 551px;
    background: var(--banner-bg);
    overflow: hidden;
    box-shadow: 5px 5px 6px var(--shadow);
  }
  .banner--first { top: 31px; }
  .banner--second { top: 613px; }

  .banner__title {
    position: absolute;
    top: 13px;
    left: 0;
    width: 100%;
    text-align: center;
    font-weight: 800;
    font-size: 82px;
    line-height: 84px;
    letter-spacing: 0.5px;
    color: var(--title-blue);
  }

  .orbit {
    position: absolute;
    left: 196px;
    top: 126px;
    width: 578px;
    height: 578px;
    border: 1.5px solid var(--orbit-line);
    border-radius: 50%;
  }
  .ring {
    position: absolute;
    left: 289px;
    top: 219px;
    width: 392px;
    height: 392px;
    border-radius: 50%;
    background: var(--ring-outer);
  }
  .portrait {
    position: absolute;
    left: 24px;
    top: 24px;
    width: 344px;
    height: 344px;
    border-radius: 50%;
  }
  .portrait--laptop {
    background: radial-gradient(circle at 50% 35%, #a9d6f7 0%, #8ccaf6 45%, #6fa3d6 100%);
  }
  .portrait--tablet {
    background: radial-gradient(circle at 50% 35%, #a9d6f7 0%, #8ccaf6 45%, #4f82c2 100%);
  }

  .pill {
    position: absolute;
    border: 2.5px solid var(--label-blue);
    border-radius: 34px;
    background: var(--banner-bg);
    display: flex;
    align-items: center;
    font-weight: 700;
    font-size: 21px;
    line-height: 23px;
    letter-spacing: 0.4px;
    color: var(--label-blue);
  }
  .pill__text { flex: 1; }
  .pill--left .pill__text { text-align: right; }
  .pill--right .pill__text { text-align: left; }
  .pill__icon {
    position: absolute;
    top: -2.5px;
    bottom: -2.5px;
    border: 2.5px solid var(--pale-line);
    background: var(--banner-bg);
    display: flex;
    align-items: center;
    justify-content: center;
  }
  .pill--left .pill__icon { right: -2.5px; border-radius: 0 34px 34px 0; border-left: none; }
  .pill--right .pill__icon { left: -2.5px; border-radius: 34px 0 0 34px; border-right: none; }
  .pill__tail { position: absolute; }

  .pill--service { left: 82px; top: 222px; width: 218px; height: 63px; padding-right: 80px; }
  .pill--service .pill__icon { width: 74px; }
  .pill--service .pill__tail { right: -14px; bottom: -12px; }

  .pill--prices { left: 23px; top: 339px; width: 236px; height: 67px; padding-left: 10px; padding-right: 72px; }
  .pill--prices .pill__icon { width: 66px; }
  .pill--prices .pill__tail { right: -22px; top: 22px; }

  .pill--staff { left: 671px; top: 222px; width: 249px; height: 63px; padding-left: 65px; }
  .pill--staff .pill__icon { width: 62px; }
  .pill--staff .pill__tail { left: -15px; bottom: 4px; }

  .pill--guarantee { left: 703px; top: 342px; width: 260px; height: 66px; padding-left: 73px; }
  .pill--guarantee .pill__icon { width: 68px; }
  .pill--guarantee .pill__tail { left: -18px; top: 22px; }

  .dollar {
    font-weight: 700;
    font-size: 38px;
    line-height: 1;
    color: var(--icon-blue);
  }
</style>
</head>
<body>
<div class="stage">

  <section class="banner banner--first">
    <h1 class="banner__title">WHY CHOOSE US</h1>
    <div class="orbit"></div>
    <div class="ring">
      <div class="portrait portrait--laptop" role="img" aria-label="Smiling man in glasses and denim shirt holding a laptop"></div>
    </div>

    <div class="pill pill--left pill--service">
      <span class="pill__text">FRIENDLY<br>SERVICE</span>
      <span class="pill__icon">
        <svg width="30" height="36" viewBox="0 0 30 36"><circle cx="15" cy="12" r="7.5" fill="var(--icon-blue)"/><path d="M5 13a10 10 0 0 1 20 0" fill="none" stroke="var(--icon-blue)" stroke-width="2.5"/><rect x="3" y="11" width="4" height="7" rx="2" fill="var(--icon-blue)"/><rect x="23" y="11" width="4" height="7" rx="2" fill="var(--icon-blue)"/><path d="M2 36c0-9 6-14 13-14s13 5 13 14z" fill="var(--icon-blue)"/></svg>
      </span>
      <svg class="pill__tail" width="20" height="20" viewBox="0 0 20 20"><path d="M2 2L18 18L4 14" fill="#fff" stroke="var(--pale-line)" stroke-width="2"/></svg>
    </div>

    <div class="pill pill--left pill--prices">
      <span class="pill__text">COMPETITIVE<br>PRICES</span>
      <span class="pill__icon"><span class="dollar">$</span></span>
      <svg class="pill__tail" width="24" height="24" viewBox="0 0 24 24"><path d="M2 3L22 12L2 21" fill="#fff" stroke="var(--pale-line)" stroke-width="2"/></svg>
    </div>

    <div class="pill pill--right pill--staff">
      <span class="pill__icon">
        <svg width="28" height="34" viewBox="0 0 28 34"><circle cx="14" cy="9" r="7.5" fill="var(--icon-blue)"/><path d="M1 34c0-10 6-15 13-15s13 5 13 15z" fill="var(--icon-blue)"/><path d="M11 19l3 10l3-10z" fill="#fff"/><rect x="17" y="25" width="6" height="3" fill="#fff"/></svg>
      </span>
      <span class="pill__text">EXPERIENCED<br>STAFF</span>
      <svg class="pill__tail" width="20" height="20" viewBox="0 0 20 20"><path d="M18 4L2 17L18 17" fill="#fff" stroke="var(--pale-line)" stroke-width="2"/></svg>
    </div>

    <div class="pill pill--right pill--guarantee">
      <span class="pill__icon">
        <svg width="32" height="36" viewBox="0 0 32 36"><path d="M16 2L29 7v10c0 9-6 15-13 17C9 32 3 26 3 17V7z" fill="var(--icon-blue)"/><circle cx="16" cy="18" r="7.5" fill="none" stroke="#fff" stroke-width="2"/><path d="M12.5 18l2.5 2.5l4.5-5" fill="none" stroke="#fff" stroke-width="2"/></svg>
      </span>
      <span class="pill__text">SATISFACTION<br>GUARANTEED</span>
      <svg class="pill__tail" width="22" height="22" viewBox="0 0 22 22"><path d="M20 3L2 11L20 19" fill="#fff" stroke="var(--pale-line)" stroke-width="2"/></svg>
    </div>
  </section>

  <section class="banner banner--second">
    <h1 class="banner__title">WHY CHOOSE US</h1>
    <div class="orbit"></div>
    <div class="ring">
      <div class="portrait portrait--tablet" role="img" aria-label="Smiling woman in blue blazer holding a tablet"></div>
    </div>

    <div class="pill pill--left pill--service">
      <span class="pill__text">FRIENDLY<br>SERVICE</span>
      <span class="pill__icon">
        <svg width="30" height="36" viewBox="0 0 30 36"><circle cx="15" cy="12" r="7.5" fill="var(--icon-blue)"/><path d="M5 13a10 10 0 0 1 20 0" fill="none" stroke="var(--icon-blue)" stroke-width="2.5"/><rect x="3" y="11" width="4" height="7" rx="2" fill="var(--icon-blue)"/><rect x="23" y="11" width="4" height="7" rx="2" fill="var(--icon-blue)"/><path d="M2 36c0-9 6-14 13-14s13 5 13 14z" fill="var(--icon-blue)"/></svg>
      </span>
      <svg class="pill__tail" width="20" height="20" viewBox="0 0 20 20"><path d="M2 2L18 18L4 14" fill="#fff" stroke="var(--pale-line)" stroke-width="2"/></svg>
    </div>

    <div class="pill pill--left pill--prices">
      <span class="pill__text">COMPETITIVE<br>PRICES</span>
      <span class="pill__icon"><span class="dollar">$</span></span>
      <svg class="pill__tail" width="24" height="24" viewBox="0 0 24 24"><path d="M2 3L22 12L2 21" fill="#fff" stroke="var(--pale-line)" stroke-width="2"/></svg>
    </div>

    <div class="pill pill--right pill--staff">
      <span class="pill__icon">
        <svg width="28" height="34" viewBox="0 0 28 34"><circle cx="14" cy="9" r="7.5" fill="var(--icon-blue)"/><path d="M1 34c0-10 6-15 13-15s13 5 13 15z" fill="var(--icon-blue)"/><path d="M11 19l3 10l3-10z" fill="#fff"/><rect x="17" y="25" width="6" height="3" fill="#fff"/></svg>
      </span>
      <span class="pill__text">EXPERIENCED<br>STAFF</span>
      <svg class="pill__tail" width="20" height="20" viewBox="0 0 20 20"><path d="M18 4L2 17L18 17" fill="#fff" stroke="var(--pale-line)" stroke-width="2"/></svg>
    </div>

    <div class="pill pill--right pill--guarantee">
      <span class="pill__icon">
        <svg width="32" height="36" viewBox="0 0 32 36"><path d="M16 2L29 7v10c0 9-6 15-13 17C9 32 3 26 3 17V7z" fill="var(--icon-blue)"/><circle cx="16" cy="18" r="7.5" fill="none" stroke="#fff" stroke-width="2"/><path d="M12.5 18l2.5 2.5l4.5-5" fill="none" stroke="#fff" stroke-width="2"/></svg>
      </span>
      <span class="pill__text">SATISFACTION<br>GUARANTEED</span>
      <svg class="pill__tail" width="22" height="22" viewBox="0 0 22 22"><path d="M20 3L2 11L20 19" fill="#fff" stroke="var(--pale-line)" stroke-width="2"/></svg>
    </div>
  </section>

</div>
</body>
</html>
```